New Design required for Disposable Gloves Pack

We need a new design for our range of disposable Gloves.
The brand name is "Marlow" I will attach the existing logo.

The needs to be 3 variations of the design (maybe different colours) that we can use for the different kinds of gloves: Latex Gloves, Clear Vinyl Gloves & Blue Vinyl Gloves.
Pack size is: 220x65x120mm.

Attached is a template to use showing all sides of the pack as flat. It is preferable that you supply an image of the complete folded pack as well with your design. Also attached is a PDF of our old pack design. Please use all the text on this old design for the new one.

The packs need to be easily differentiated from each other.

Target Market(s)

New Zealand Businesses, food processors & manufacturers. Medical & health care professionals

Font styles to use
Sans Serif

Requirements
Must have
• 3 variations of the same pack design to differentiate between the 3 types of gloves we offer: Latex Gloves, Clear Vinyl & Blue Vinyl Gloves.

```html
<!DOCTYPE html>
<html lang="en">
<head>
<meta charset="utf-8">
<title>Marlow Disposable Gloves – Pack Dielines</title>
<link rel="stylesheet" href="https://fonts.googleapis.com/css2?family=Cabin:wght@500;600;700&family=Arimo:ital,wght@0,700;1,400&display=swap">
<style>
  :root {
    --page: #ffffff;
    --white: #ffffff;
    --glove-art: #bfe6f5;
    --curve-light: #e4f8fd;

    --latex-main: #ab1468;
    --latex-dark: #6e0b47;
    --latex-accent: #ff6ec9;
    --latex-phone: #ff8fd3;
    --latex-photo-a: #d98dbd;
    --latex-photo-b: #b784b0;
    --latex-word: #6e0b47;

    --blue-main: #0b6ec5;
    --blue-dark: #0c3d8f;
    --blue-accent: #4fb3ff;
    --blue-phone: #7cc6ff;
    --blue-photo-a: #6fb0e0;
    --blue-photo-b: #5a9cc8;
    --blue-word: #0c3a8c;

    --green-main: #2b8a31;
    --green-dark: #1c6a22;
    --green-accent: #37a33e;
    --green-phone: #b5f0b9;
    --green-photo-a: #9fd896;
    --green-photo-b: #6fbf6a;
    --green-word: #aaf0b4;
  }

  * { box-sizing: border-box; margin: 0; padding: 0; }

  html, body {
    width: 1200px;
    height: 846px;
    overflow: hidden;
    background: var(--page);
  }

  .canvas {
    position: relative;
    width: 1200px;
    height: 846px;
    overflow: hidden;
    background: var(--page);
    font-family: "Cabin", "Trebuchet MS", sans-serif;
  }

  /* ---------- Dieline ---------- */
  .dieline {
    position: absolute;
    width: 567px;
    height: 378px;
  }
  .dieline--latex { left: 22px;  top: 45px;  --main: var(--latex-main); --dark: var(--latex-dark); --accent: var(--latex-accent); --phone: var(--latex-phone); --photo-a: var(--latex-photo-a); --photo-b: var(--latex-photo-b); --word: var(--latex-word); }
  .dieline--blue  { left: 612px; top: 45px;  --main: var(--blue-main);  --dark: var(--blue-dark);  --accent: var(--blue-accent);  --phone: var(--blue-phone);  --photo-a: var(--blue-photo-a);  --photo-b: var(--blue-photo-b);  --word: var(--blue-word); }
  .dieline--green { left: 27px;  top: 452px; --main: var(--green-main); --dark: var(--green-dark); --accent: var(--green-accent); --phone: var(--green-phone); --photo-a: var(--green-photo-a); --photo-b: var(--green-photo-b); --word: var(--green-word); }

  .panel-main {
    position: absolute;
    left: 148px;
    top: 0;
    width: 270px;
    height: 378px;
    background: var(--main);
    overflow: hidden;
  }

  .backdrop {
    position: absolute;
    left: 0; top: 0;
    width: 270px; height: 229px;
    background: linear-gradient(160deg, var(--photo-a) 0%, var(--photo-b) 70%, var(--photo-a) 100%);
  }

  .curve {
    position: absolute;
    left: 0; top: 0;
    width: 270px; height: 150px;
  }
  .curve .c-dark   { fill: var(--dark); }
  .curve .c-accent { fill: var(--accent); }
  .curve .c-light  { fill: var(--curve-light); }

  .glove-art {
    position: absolute;
    left: 210px; top: 30px;
    width: 56px; height: 108px;
    border-radius: 40% 40% 30% 30%;
    background: var(--glove-art);
  }

  .brand {
    position: absolute;
    display: flex;
    align-items: center;
    gap: 5px;
    color: var(--white);
    font-weight: 600;
    letter-spacing: 1px;
  }
  .brand__dot {
    border-radius: 50%;
    background: var(--white);
  }
  .brand--front { left: 34px; top: 30px; font-size: 21px; }
  .brand--front .brand__dot { width: 9px; height: 9px; }

  .product-name {
    position: absolute;
    line-height: 1;
  }
  .product-name__kind {
    display: block;
    font-variant: small-caps;
    font-weight: 700;
    color: var(--white);
  }
  .product-name__gloves {
    display: block;
    font-weight: 600;
    color: var(--word);
  }
  .product-name--front { left: 12px; top: 80px; }
  .product-name--front .product-name__kind { font-size: 20px; }
  .product-name--front .product-name__gloves { font-size: 30px; margin-top: 2px; }
  .product-name--top { left: 10px; top: 160px; }
  .product-name--top .product-name__kind { font-size: 20px; }
  .product-name--top .product-name__gloves { font-size: 30px; margin-top: 2px; }

  .features {
    position: absolute;
    left: 170px; top: 170px;
    list-style: none;
    font-family: "Arimo", Arial, sans-serif;
    font-style: italic;
    font-size: 10.5px;
    color: var(--white);
  }
  .features li {
    position: relative;
    padding-left: 13px;
    margin-bottom: 4px;
  }
  .features li::before {
    content: "";
    position: absolute;
    left: 0; top: 3px;
    width: 6px; height: 6px;
    border-radius: 50%;
    background: var(--white);
  }

  .size-bar {
    position: absolute;
    left: 0; top: 221px;
    width: 270px; height: 8px;
    background: var(--dark);
  }
  .size-bar__label {
    position: absolute;
    left: 22px; top: -3px;
    font-size: 9px;
    color: var(--white);
    letter-spacing: .5px;
  }

  /* ---------- Side flaps ---------- */
  .flap {
    position: absolute;
    top: 149px;
    width: 149px;
    height: 80px;
    background: var(--main);
    color: var(--white);
  }
  .flap--left  { left: 0; }
  .flap--right { left: 418px; }

  .brand--flap { left: 46px; top: 12px; font-size: 13px; letter-spacing: .5px; }
  .brand--flap .brand__dot { width: 5px; height: 5px; }

  .flap__phone {
    position: absolute;
    left: 36px; top: 49px;
    font-family: "Arimo", Arial, sans-serif;
    font-size: 12px;
    color: var(--phone);
  }
  .flap__web {
    position: absolute;
    left: 37px; top: 65px;
    font-family: "Arimo", Arial, sans-serif;
    font-weight: 700;
    font-size: 8px;
  }
</style>
</head>
<body>
<main class="canvas">

  <!-- Latex variant -->
  <section class="dieline dieline--latex" aria-label="Latex gloves pack dieline">
    <div class="flap flap--left">
      <div class="brand brand--flap"><span class="brand__dot"></span>Marlow</div>
      <p class="flap__phone">0800 555 019</p>
      <p class="flap__web">www.harbourpak.co.nz</p>
    </div>
    <div class="panel-main">
      <div class="backdrop" role="img" aria-label="Soft-focus leaf photograph tinted pink"></div>
      <svg class="curve" viewBox="0 0 270 150" aria-hidden="true">
        <path class="c-accent" d="M178 0 Q196 105 270 150 L270 0 Z"/>
        <path class="c-dark" d="M186 0 Q203 100 270 142 L270 0 Z"/>
        <path class="c-light" d="M200 0 Q214 92 270 132 L270 0 Z"/>
      </svg>
      <div class="glove-art" role="img" aria-label="Illustration of a blue disposable glove"></div>
      <div class="brand brand--front"><span class="brand__dot"></span>Marlow</div>
      <h2 class="product-name product-name--front"><span class="product-name__kind">Latex</span><span class="product-name__gloves">GLOVES</span></h2>
      <h3 class="product-name product-name--top"><span class="product-name__kind">Latex</span><span class="product-name__gloves">GLOVES</span></h3>
      <ul class="features"><li>Ambidexterous</li><li>Singe use</li><li>Lightly powered</li></ul>
      <div class="size-bar"><span class="size-bar__label">LARGE</span></div>
    </div>
    <div class="flap flap--right">
      <div class="brand brand--flap"><span class="brand__dot"></span>Marlow</div>
      <p class="flap__phone">0800 555 019</p>
      <p class="flap__web">www.harbourpak.co.nz</p>
    </div>
  </section>

  <!-- Blue vinyl variant -->
  <section class="dieline dieline--blue" aria-label="Blue vinyl gloves pack dieline">
    <div class="flap flap--left">
      <div class="brand brand--flap"><span class="brand__dot"></span>Marlow</div>
      <p class="flap__phone">0800 555 019</p>
      <p class="flap__web">www.harbourpak.co.nz</p>
    </div>
    <div class="panel-main">
      <div class="backdrop" role="img" aria-label="Soft-focus leaf photograph tinted blue"></div>
      <svg class="curve" viewBox="0 0 270 150" aria-hidden="true">
        <path class="c-accent" d="M178 0 Q196 105 270 150 L270 0 Z"/>
        <path class="c-dark" d="M186 0 Q203 100 270 142 L270 0 Z"/>
        <path class="c-light" d="M200 0 Q214 92 270 132 L270 0 Z"/>
      </svg>
      <div class="glove-art" role="img" aria-label="Illustration of a blue disposable glove"></div>
      <div class="brand brand--front"><span class="brand__dot"></span>Marlow</div>
      <h2 class="product-name product-name--front"><span class="product-name__kind">Blue Vinyl</span><span class="product-name__gloves">GLOVES</span></h2>
      <h3 class="product-name product-name--top"><span class="product-name__kind">Blue Vinyl</span><span class="product-name__gloves">GLOVES</span></h3>
      <ul class="features"><li>Ambidexterous</li><li>Singe use</li><li>Lightly powered</li></ul>
      <div class="size-bar"><span class="size-bar__label">LARGE</span></div>
    </div>
    <div class="flap flap--right">
      <div class="brand brand--flap"><span class="brand__dot"></span>Marlow</div>
      <p class="flap__phone">0800 555 019</p>
      <p class="flap__web">www.harbourpak.co.nz</p>
    </div>
  </section>

  <!-- Clear vinyl variant -->
  <section class="dieline dieline--green" aria-label="Clear vinyl gloves pack dieline">
    <div class="flap flap--left">
      <div class="brand brand--flap"><span class="brand__dot"></span>Marlow</div>
      <p class="flap__phone">0800 555 019</p>
      <p class="flap__web">www.harbourpak.co.nz</p>
    </div>
    <div class="panel-main">
      <div class="backdrop" role="img" aria-label="Soft-focus leaf photograph tinted green"></div>
      <svg class="curve" viewBox="0 0 270 150" aria-hidden="true">
        <path class="c-accent" d="M178 0 Q196 105 270 150 L270 0 Z"/>
        <path class="c-dark" d="M186 0 Q203 100 270 142 L270 0 Z"/>
        <path class="c-light" d="M200 0 Q214 92 270 132 L270 0 Z"/>
      </svg>
      <div class="glove-art" role="img" aria-label="Illustration of a blue disposable glove"></div>
      <div class="brand brand--front"><span class="brand__dot"></span>Marlow</div>
      <h2 class="product-name product-name--front"><span class="product-name__kind">Clear Vinyl</span><span class="product-name__gloves">GLOVES</span></h2>
      <h3 class="product-name product-name--top"><span class="product-name__kind">Clear Vinyl</span><span class="product-name__gloves">GLOVES</span></h3>
      <ul class="features"><li>Ambidexterous</li><li>Singe use</li><li>Lightly powered</li></ul>
      <div class="size-bar"><span class="size-bar__label">LARGE</span></div>
    </div>
    <div class="flap flap--right">
      <div class="brand brand--flap"><span class="brand__dot"></span>Marlow</div>
      <p class="flap__phone">0800 555 019</p>
      <p class="flap__web">www.harbourpak.co.nz</p>
    </div>
  </section>

</main>
</body>
</html>
```